Business Card for Wellness Clinic

We need a business card for our new logo. I want it to match the feel of the logo

Target Market(s)

Young professional families looking for holistic health care

Industry/Entity Type

Health And Wellness

Contact Information for Business Card

Our business Name: Brackenfield Health & wellness Centre, our phone #, email address...see attached old business card

Font styles to use
Sans Serif

Colors
33b8a4
cee9f5

Requirements
Must have
• my logo and business name
• Font is "Helvetica Neue LT Std 45 Light" and
• Only for "&" using font "Trajan pro bold"
• Use colors in the logo

```html
<!DOCTYPE html>
<html lang="en">
<head>
<meta charset="utf-8">
<title>Brackenfield Health &amp; wellness Centre – Business Cards</title>
<link href="https://fonts.googleapis.com/css2?family=Roboto:wght@300;400&display=swap" rel="stylesheet">
<style>
  :root {
    --teal: #1fb09c;
    --teal-soft: #33b8a4;
    --ink: #2b2b2b;
    --curve-dark: #3a3a3a;
    --paper: #ffffff;
    --page: #eef1f2;
    --muted: #555b5e;
  }
  * { box-sizing: border-box; margin: 0; padding: 0; }
  html, body { width: 1200px; height: 1200px; overflow: hidden; }
  body {
    background: var(--page);
    font-family: "Roboto", "Helvetica Neue", Arial, sans-serif;
    font-weight: 300;
    position: relative;
  }
  .card {
    position: absolute;
    left: 250px;
    width: 700px;
    height: 400px;
    background: var(--paper);
    box-shadow: 0 6px 22px rgba(0,0,0,0.12);
    overflow: hidden;
  }
  .card-bg { position: absolute; inset: 0; }

  /* Contact side */
  .card--contact { top: 130px; }
  .contact-name {
    position: absolute; left: 300px; top: 34px;
    color: var(--paper); font-size: 40px; line-height: 1.05; font-weight: 300;
  }
  .contact-practitioner {
    position: absolute; left: 300px; top: 128px;
    color: var(--paper); font-size: 17px;
  }
  .contact-details {
    position: absolute; left: 360px; top: 178px;
    color: var(--paper); font-size: 15px; line-height: 1.5;
  }
  .icon-pin { position: absolute; left: 318px; top: 186px; }
  .contact-web {
    position: absolute; right: 28px; bottom: 26px;
    display: flex; gap: 26px; color: var(--paper); font-size: 14px;
  }
  .contact-web span { display: flex; align-items: center; gap: 8px; }
  .logo-mark {
    position: absolute; width: 92px; height: 92px;
    background: var(--teal); border-radius: 8px;
  }
  .card--contact .logo-mark { left: 70px; top: 270px; }

  /* Appointment side */
  .card--appointment { top: 650px; }
  .card--appointment .logo-mark { left: 48px; top: 150px; }
  .appt-name {
    position: absolute; left: 290px; top: 42px;
    color: var(--teal); font-size: 44px; line-height: 1.05; font-weight: 300;
  }
  .appt-form {
    position: absolute; left: 290px; top: 200px; width: 380px;
    color: var(--ink); font-size: 16px;
  }
  .form-row { display: flex; align-items: flex-end; gap: 8px; margin-bottom: 22px; }
  .form-line { flex: 1; border-bottom: 1.5px solid var(--ink); height: 1px; }
  .appt-note {
    position: absolute; left: 290px; bottom: 34px; width: 390px;
    color: var(--muted); font-size: 13px; line-height: 1.45; text-align: center;
  }
</style>
</head>
<body>

  <!-- Contact card -->
  <section class="card card--contact" aria-label="Business card, contact side">
    <svg class="card-bg" width="700" height="400" viewBox="0 0 700 400">
      <rect width="700" height="400" fill="#1fb09c"/>
      <path d="M0 215 Q210 185 300 400 L0 400 Z" fill="#ffffff"/>
      <path d="M0 215 Q210 185 300 400" fill="none" stroke="#3a3a3a" stroke-width="5"/>
    </svg>
    <div class="logo-mark" aria-hidden="true"></div>
    <h1 class="contact-name">Brackenfield Health &amp;<br>wellness Centre</h1>
    <p class="contact-practitioner">Dr. Maren Holt, N.D. &nbsp;·&nbsp; Naturopathic Doctor</p>
    <svg class="icon-pin" width="26" height="26" viewBox="0 0 26 26" aria-hidden="true">
      <circle cx="13" cy="13" r="12" fill="#ffffff"/>
      <path d="M13 6a5 5 0 0 0-5 5c0 4 5 9 5 9s5-5 5-9a5 5 0 0 0-5-5z" fill="#1fb09c"/>
      <circle cx="13" cy="11" r="1.8" fill="#ffffff"/>
    </svg>
    <p class="contact-details">48 Larchmont Ave, Suite 12<br>Halden, ON K0L 2B1<br>555-014-2287</p>
    <div class="contact-web">
      <span>
        <svg width="18" height="18" viewBox="0 0 18 18" aria-hidden="true"><circle cx="9" cy="9" r="8.5" fill="#fff"/><circle cx="9" cy="9" r="4.5" fill="none" stroke="#1fb09c" stroke-width="1.4"/><path d="M4.5 9h9M9 4.5v9" stroke="#1fb09c" stroke-width="1.2"/></svg>
        haldennaturopathic.ca
      </span>
      <span>
        <svg width="18" height="18" viewBox="0 0 18 18" aria-hidden="true"><circle cx="9" cy="9" r="8.5" fill="#fff"/><rect x="4.5" y="6" width="9" height="6.5" fill="none" stroke="#1fb09c" stroke-width="1.3"/><path d="M4.5 6l4.5 4 4.5-4" fill="none" stroke="#1fb09c" stroke-width="1.3"/></svg>
        mholt@haldennaturopathic.ca
      </span>
    </div>
  </section>

  <!-- Appointment card -->
  <section class="card card--appointment" aria-label="Business card, appointment side">
    <svg class="card-bg" width="700" height="400" viewBox="0 0 700 400">
      <path d="M200 0 Q175 200 245 400 L262 400 Q195 200 212 0 Z" fill="#33b8a4"/>
      <path d="M212 0 Q200 200 262 400 L272 400 Q212 200 220 0 Z" fill="#e4e6e6"/>
    </svg>
    <div class="logo-mark" aria-hidden="true"></div>
    <h2 class="appt-name">Brackenfield Health &amp;<br>wellness Centre</h2>
    <div class="appt-form">
      <div class="form-row"><span>Date</span><span class="form-line"></span><span>Time</span><span class="form-line"></span></div>
      <div class="form-row"><span>For</span><span class="form-line"></span></div>
    </div>
    <p class="appt-note">If you are unable to keep your appointment, please provide at least 2 business day notice or full visit fees will apply.</p>
  </section>

</body>
</html>
```